Creative & Professional Business Card for hair salon

We are looking to update our business cards. Our salon is creative, modern, progressive and professional and looking for a design that will reflect this.

```html
<!DOCTYPE html>
<html lang="en">
<head>
<meta charset="utf-8">
<title>Airy Strands – Appointment Card</title>
<link rel="stylesheet" href="https://fonts.googleapis.com/css2?family=Quicksand:wght@300;400&family=Arimo:wght@400;700&display=swap">
<style>
  :root {
    --paper: #ffffff;
    --brand: #4a7592;
    --ink: #3d5f7c;
    --rule: #8faab9;
    --sky-top: #3f9de0;
    --sky-mid: #cfeaf6;
    --sky-low: #bfe5f3;
    --sky-bottom: #9fdaee;
    --white: #ffffff;
  }
  html, body {
    margin: 0;
    padding: 0;
    width: 1050px;
    height: 1200px;
    overflow: hidden;
    background: var(--paper);
  }
  .card {
    position: relative;
    width: 1050px;
    height: 1200px;
    overflow: hidden;
  }
  .brand-panel {
    position: absolute;
    inset: 0 0 auto 0;
    height: 600px;
    background: var(--paper);
  }
  .brand-name {
    position: absolute;
    right: 165px;
    top: 322px;
    margin: 0;
    font-family: "Quicksand", sans-serif;
    font-weight: 300;
    font-size: 76px;
    line-height: 1;
    color: var(--brand);
    letter-spacing: -1px;
  }
  .brand-owner {
    position: absolute;
    right: 180px;
    top: 418px;
    margin: 0;
    font-family: "Quicksand", sans-serif;
    font-weight: 300;
    font-size: 40px;
    color: var(--brand);
  }
  .appointment-panel {
    position: absolute;
    left: 0;
    top: 600px;
    width: 1050px;
    height: 600px;
  }
  .sky {
    position: absolute;
    inset: 0;
    background: linear-gradient(180deg,
      var(--sky-top) 0%,
      #7cc0ea 16%,
      var(--sky-mid) 38%,
      var(--sky-low) 65%,
      var(--sky-bottom) 100%);
  }
  .appointment-title {
    position: absolute;
    top: 36px;
    left: 0;
    width: 1075px;
    margin: 0;
    text-align: center;
    font-family: "Quicksand", sans-serif;
    font-weight: 400;
    font-size: 38px;
    color: var(--white);
  }
  .write-line {
    position: absolute;
    right: 128px;
    height: 0;
    border-top: 1px solid var(--rule);
  }
  .write-line--first { top: 217px; left: 150px; }
  .write-line--second { top: 331px; left: 125px; }
  .contact {
    position: absolute;
    left: 0;
    top: 424px;
    width: 1075px;
    text-align: center;
    font-family: "Arimo", sans-serif;
    color: var(--ink);
  }
  .contact p { margin: 0; }
  .contact-address { font-weight: 700; font-size: 36px; line-height: 44px; }
  .contact-phone { font-weight: 700; font-size: 28px; line-height: 34px; }
  .contact-line { font-size: 28px; line-height: 36px; }
  .contact svg { vertical-align: -4px; margin-right: 6px; }
  .gap { display: inline-block; width: 22px; }
</style>
</head>
<body>
<main class="card">
  <header class="brand-panel">
    <h1 class="brand-name">Airy Strands</h1>
    <p class="brand-owner">by Lena Marlow</p>
  </header>

  <section class="appointment-panel">
    <div class="sky" role="img" aria-label="Photograph of a blue sky with soft white clouds"></div>
    <h2 class="appointment-title">Your next appointment is:</h2>
    <div class="write-line write-line--first"></div>
    <div class="write-line write-line--second"></div>

    <address class="contact" style="font-style:normal">
      <p class="contact-address">5/22 Hollis Street, Maroochy</p>
      <p class="contact-phone">
        <svg width="20" height="28" viewBox="0 0 20 28" aria-hidden="true"><path d="M5 2 L9 2 L10 8 L7 10 Q8 16 12 20 L15 18 L19 21 L18 26 Q10 27 5 17 Q1 9 5 2 Z" fill="var(--ink)"/></svg>07 5550 0142
      </p>
      <p class="contact-line">
        <svg width="34" height="24" viewBox="0 0 34 24" aria-hidden="true"><rect x="1" y="1" width="32" height="22" fill="none" stroke="var(--ink)" stroke-width="2"/><path d="M1 1 L17 14 L33 1 M1 23 L13 11 M33 23 L21 11" fill="none" stroke="var(--ink)" stroke-width="2"/></svg>salon@airystrands.com.au<span class="gap"></span><svg width="30" height="30" viewBox="0 0 30 30" aria-hidden="true"><circle cx="15" cy="15" r="13" fill="none" stroke="var(--ink)" stroke-width="2"/><ellipse cx="15" cy="15" rx="6" ry="13" fill="none" stroke="var(--ink)" stroke-width="1.5"/><path d="M2 15 H28 M4 8 H26 M4 22 H26" stroke="var(--ink)" stroke-width="1.5"/></svg>www.airystrands.com.au
      </p>
      <p class="contact-line">
        <svg width="28" height="28" viewBox="0 0 28 28" aria-hidden="true"><circle cx="14" cy="14" r="12.5" fill="none" stroke="var(--ink)" stroke-width="2"/></svg>www.social.example/AiryStrandsbyLenaMarlow
      </p>
    </address>
  </section>
</main>
</body>
</html>
```